Design for a Service-Based Estimate

We want a design for an Estimate that will always be sent in PDF format. The estimate or proposal is a critical document that needs to plainly show the service items, item description but also needs to be attractive and professional looking. Our current estimate deliverable is attached but it looks really basic like a Word document

```html
<!DOCTYPE html>
<html lang="en">
<head>
<meta charset="utf-8">
<title>Firm Slab – Cost Estimate</title>
<link rel="stylesheet" href="https://fonts.googleapis.com/css2?family=Montserrat:wght@400;500;600;700;800&family=Open+Sans:wght@400;600;700&display=swap">
<style>
  :root {
    --backdrop: #3a302b;
    --navy: #3e3c55;
    --slate: #7f7c8d;
    --paper-grey: #e9e7e5;
    --watermark: #dcd8d4;
    --white: #ffffff;
    --ink: #2f2d44;
    --muted: #8a8580;
    --rule: #e2e0de;
    --orange: #d4542b;
  }
  * { box-sizing: border-box; margin: 0; padding: 0; }
  html, body { width: 1200px; height: 834px; overflow: hidden; }
  body {
    background: var(--backdrop);
    font-family: "Montserrat", sans-serif;
    color: var(--ink);
    position: relative;
  }
  .page {
    position: absolute;
    top: 74px;
    width: 523px;
    height: 675px;
    background: var(--paper-grey);
    overflow: hidden;
  }
  .page--estimate { left: 67px; }
  .page--terms { left: 608px; }

  .page__title-bar {
    height: 28px;
    background: var(--navy);
    color: var(--white);
    font-size: 10px;
    font-weight: 600;
    letter-spacing: 1.2px;
    text-align: center;
    line-height: 28px;
  }
  .page__brand-band {
    height: 42px;
    background: var(--white);
    display: flex;
    align-items: center;
    justify-content: center;
  }
  .brand-name {
    font-family: "Montserrat", sans-serif;
    font-weight: 800;
    color: var(--navy);
    letter-spacing: 1px;
    white-space: nowrap;
  }
  .page__brand-band .brand-name { font-size: 27px; }
  .page__contact {
    text-align: center;
    font-size: 10px;
    font-weight: 600;
    color: var(--ink);
    margin-top: 7px;
  }

  .card {
    position: absolute;
    left: 30px;
    top: 114px;
    width: 463px;
    height: 418px;
    background: var(--white);
    border-radius: 6px;
  }

  /* Estimate card */
  .recipient { position: absolute; left: 12px; top: 17px; }
  .recipient__label { font-size: 7px; font-weight: 700; color: var(--muted); letter-spacing: .5px; }
  .recipient__name {
    font-size: 21px; font-weight: 500; line-height: 25px; color: var(--ink);
    margin-top: 6px;
  }
  .recipient__details { font-size: 7.5px; font-weight: 700; line-height: 13px; margin-top: 5px; }
  .bid-number {
    position: absolute; right: 30px; top: 13px;
    font-size: 11px; font-weight: 700; letter-spacing: 1.5px;
  }

  .line-items {
    position: absolute; left: 0; top: 131px; width: 100%;
    border-collapse: collapse; font-size: 10.5px;
  }
  .line-items th {
    background: var(--slate); color: var(--white);
    font-weight: 500; height: 25px; text-align: center;
  }
  .line-items td { height: 25px; text-align: center; font-weight: 500; border-bottom: 1px solid var(--rule); }
  .line-items .col-item { text-align: left; padding-left: 12px; width: 190px; }
  .line-items .col-qty { width: 70px; }
  .line-items .col-um { width: 50px; }
  .line-items .col-unit { width: 65px; }
  .line-items .col-total { text-align: right; padding-right: 14px; }

  .total-bar {
    position: absolute; left: 0; top: 256px; width: 100%; height: 37px;
    background: var(--navy); color: var(--white);
    display: flex; align-items: center; justify-content: flex-end;
    padding-right: 14px; gap: 40px;
  }
  .total-bar__label { font-size: 9.5px; font-weight: 500; }
  .total-bar__amount { font-size: 13px; font-weight: 700; }

  .acknowledgement {
    position: absolute; left: 47px; top: 336px;
    display: flex; align-items: center; gap: 8px;
    font-size: 8px; font-weight: 500;
  }
  .acknowledgement__box { width: 10px; height: 10px; border: 1px solid #9c9894; border-radius: 2px; }
  .sign-field { position: absolute; top: 372px; width: 156px; border-bottom: 1px solid #8e8a86; height: 25px; }
  .sign-field--date { left: 48px; }
  .sign-field--signature { left: 255px; }
  .sign-field__label { font-size: 6.5px; font-weight: 700; color: var(--muted); letter-spacing: 1px; }

  /* Terms card */
  .terms { padding: 42px 40px 0 52px; font-family: "Open Sans", sans-serif; }
  .terms__title { text-align: center; font-size: 10px; font-weight: 700; margin-bottom: 17px; color: #222; }
  .terms__list { list-style: disc; font-size: 7px; line-height: 11.4px; color: #222; font-weight: 600; }
  .terms__list li { margin-left: 8px; }

  .page__watermark {
    position: absolute; left: 0; right: 0; top: 556px;
    text-align: center;
  }
  .page__watermark .brand-name { font-size: 70px; color: var(--watermark); letter-spacing: 2px; }
  .page__footer {
    position: absolute; left: 0; right: 0; top: 631px; height: 29px;
    background: var(--white);
    display: flex; align-items: center; justify-content: center;
  }
  .page__footer .brand-name { font-size: 11px; }
  .page__accent { position: absolute; left: 0; right: 0; top: 660px; height: 15px; background: var(--orange); }
</style>
</head>
<body>

<section class="page page--estimate">
  <div class="page__title-bar">COST ESTIMATE</div>
  <div class="page__brand-band"><span class="brand-name">FIRM SLAB</span></div>
  <p class="page__contact">48 Harbor Lane Easton 20145&nbsp; hello@firmslab.com</p>

  <div class="card">
    <div class="recipient">
      <p class="recipient__label">TO</p>
      <h1 class="recipient__name">Dana Whitcombe<br>New Concrete Pad</h1>
      <p class="recipient__details">48 Harbor Lane Easton 20145<br>client@email.com</p>
    </div>
    <p class="bid-number">BID # 200182</p>

    <table class="line-items">
      <thead>
        <tr><th class="col-item">Item</th><th class="col-qty">Quantity</th><th class="col-um">U/M</th><th class="col-unit">Unit $</th><th class="col-total">Total</th></tr>
      </thead>
      <tbody>
        <tr><td class="col-item">Item Description</td><td>576</td><td>SF</td><td>$8.65</td><td class="col-total">$4,982.40</td></tr>
        <tr><td class="col-item">Item Description</td><td>576</td><td>SF</td><td>$8.65</td><td class="col-total">$4,982.40</td></tr>
        <tr><td class="col-item">Item Description</td><td>576</td><td>SF</td><td>$8.65</td><td class="col-total">$4,982.40</td></tr>
        <tr><td class="col-item">Item Description</td><td>576</td><td>SF</td><td>$8.65</td><td class="col-total">$4,982.40</td></tr>
      </tbody>
    </table>

    <div class="total-bar">
      <span class="total-bar__label">TOTAL COST</span>
      <span class="total-bar__amount">$4,982.40</span>
    </div>

    <label class="acknowledgement">
      <span class="acknowledgement__box"></span>
      I have read Terms &amp; Conditions carefully which is printed at the back of this page.
    </label>
    <div class="sign-field sign-field--date"><span class="sign-field__label">DATE</span></div>
    <div class="sign-field sign-field--signature"><span class="sign-field__label">CLIENT SIGNATURE</span></div>
  </div>

  <div class="page__watermark" aria-hidden="true"><span class="brand-name">FIRM SLAB</span></div>
  <div class="page__footer"><span class="brand-name">FIRM SLAB</span></div>
  <div class="page__accent"></div>
</section>

<section class="page page--terms">
  <div class="page__title-bar">COST ESTIMATE</div>
  <div class="page__brand-band"><span class="brand-name">FIRM SLAB</span></div>
  <p class="page__contact">48 Harbor Lane Easton 20145&nbsp; hello@firmslab.com</p>

  <div class="card terms">
    <h2 class="terms__title">Terms and Conditions</h2>
    <ul class="terms__list">
      <li>Prices as quoted in this estimate are valid for (60) days only.</li>
      <li>Payment in full, less any previously paid amounts, is due to the Contractor upon completion of the proposed scope of work.</li>
      <li>All change order requests must be communicated in writing to the Contractor by the Client or their authorized representative.</li>
      <li>All measurements listed in this estimate are approximate and may vary slightly due to actual field conditions.</li>
      <li>It is agreed by the Contractor and the Client that complications and costs arising from unforeseen conditions and handling of unsuitable materials are not included in this estimate.</li>
      <li>Unless specifically listed in this estimate, the following items and their costs are not included: Maintenance of Traffic, Concrete Material Pumping, Testing, Excavation, Grading and Fill Material, Permits and Fees, Surveying and As-builts, Irrigation Repair, Landscaping and Root Mitigation, De-watering, Private Locates and Accessibility.</li>
      <li>Private utility locating services using radio detection devices and, when necessary, ground penetrating radar are offered by Firm Slab to assist in finding private utilities that may not have been located by the public one call system. Firm Slab will not be responsible for private utilities that have not been located nor for the failure of the above equipment to accurately detect existing utilities since the equipment is fallible and existing site conditions may preclude the ability of the equipment to detect an identifiable signal.</li>
    </ul>
  </div>

  <div class="page__watermark" aria-hidden="true"><span class="brand-name">FIRM SLAB</span></div>
  <div class="page__footer"><span class="brand-name">FIRM SLAB</span></div>
  <div class="page__accent"></div>
</section>

</body>
</html>
```